The Gallowmere Notes Theatre Production Poster

We're after a poster for a theatre production based on R.T Ambrey's book, The Gallowmere Notes.
This play follows the story of a senior demon teaching a student demon how to tempt humankind. The tone of the play is light and formal with dark undertones and moments of levity. Hell is set in a university. I am wanting an eye-catching poster. Something subtle and NOT in the theme of 'horror'. I am open to different creative ideas, but I like the idea of a book being involved and maybe some shadow loosely representing a demon reading the book. Another idea could be a shadow hovering over a silhouetted human.
Other details that the poster must include:
- The Name of the Show: The Gallowmere Notes
- Time of the shows: 7:30 pm
- Dates of the show: Saturday 8th and 15th of October 2022
- Location: Brindlecombe Civic Theatre
- Organisation: Lanterngate Theatre Productions
- ticket price: $38
- bookings made at: https://app.seatvane-example.org.au/LanterngateTheatreProductions/Gallowmere
Target Market(s)
university Students
Industry/Entity Type
Theatre
Look and feel
Each slider illustrates characteristics of the customer's brand and the style your logo design should communicate.

```html
<!DOCTYPE html>
<html lang="en">
<head>
<meta charset="utf-8">
<title>The Gallowmere Notes – Theatre Poster</title>
<link href="https://fonts.googleapis.com/css2?family=Mr+Dafoe&family=Cinzel:wght@400;500&family=Poppins:wght@400;600;700&family=Bebas+Neue&family=Montserrat:wght@300;400&display=swap" rel="stylesheet">
<style>
  :root {
    --backdrop: #cfcfcf;
    --ink: #0c0c0d;
    --white: #ffffff;
    --red: #e4151b;
    --grey-light: #6e6e6e;
    --grey-mid: #3a3a3b;
    --label-grey: #bdbdbd;
  }
  * { margin: 0; padding: 0; box-sizing: border-box; }
  html, body {
    width: 765px; height: 1200px; overflow: hidden;
    background: var(--backdrop);
  }
  .poster {
    position: absolute; left: 22px; top: 90px;
    width: 720px; height: 1019px;
    background: var(--ink);
    overflow: hidden;
    box-shadow: 4px 6px 12px rgba(0,0,0,0.35);
  }
  .poster__photo {
    position: absolute; inset: 0 0 260px 0;
    background:
      linear-gradient(212deg, var(--grey-light) 0%, #4b4b4c 22%, var(--grey-mid) 40%, #1b1b1c 62%, var(--ink) 100%);
  }
  .producer {
    position: absolute; top: 46px; left: 0; width: 100%;
    text-align: center;
    font-family: "Montserrat", sans-serif; font-weight: 300;
    font-size: 12px; letter-spacing: 8px;
    color: var(--label-grey); text-transform: uppercase;
  }
  .title { position: absolute; left: 0; top: 0; width: 100%; }
  .title span { position: absolute; font-family: "Mr Dafoe", cursive; line-height: 1; white-space: nowrap; }
  .title__the   { left: 186px; top: 458px; font-size: 68px; color: var(--white); }
  .title__main  { left: 58px;  top: 500px; font-size: 132px; color: var(--red); }
  .title__notes { left: 230px; top: 615px; font-size: 140px; color: var(--white); }

  .date-box {
    position: absolute; left: 63px; top: 806px; width: 98px; height: 121px;
    border: 2px solid var(--red);
    font-family: "Cinzel", serif; color: var(--white); text-align: center;
  }
  .date-box__day { font-size: 34px; line-height: 1; display: block; }
  .date-box__day sup { font-size: 22px; vertical-align: 9px; }
  .date-box__first { margin-top: 10px; }
  .date-box__amp {
    display: block; width: 17px; height: 17px; margin: 3px auto 2px;
    border-radius: 50%; background: var(--red);
    font-family: "Poppins", sans-serif; font-size: 11px; line-height: 17px;
  }
  .month {
    position: absolute; left: 168px; top: 800px;
    font-family: "Cinzel", serif; font-size: 37px; color: var(--white); line-height: 1;
  }
  .weekday {
    position: absolute; left: 170px; top: 843px;
    font-family: "Montserrat", sans-serif; font-size: 19px; letter-spacing: 6px; color: var(--white);
  }
  .showtime {
    position: absolute; left: 171px; top: 874px; width: 179px; height: 51px;
    background: var(--red); color: var(--white);
    font-family: "Poppins", sans-serif; font-weight: 700; font-size: 35px;
    line-height: 53px; text-align: center;
  }
  .source {
    position: absolute; left: 392px; top: 803px;
    font-family: "Poppins", sans-serif; font-size: 16px; color: var(--white); letter-spacing: -0.3px;
  }
  .source strong { font-weight: 700; }
  .ticket {
    position: absolute; left: 392px; top: 836px; width: 265px; height: 62px;
    border: 1.5px solid var(--red); display: flex;
  }
  .ticket__label {
    flex: 1; font-family: "Bebas Neue", sans-serif; font-size: 33px;
    color: var(--white); line-height: 60px; text-align: center;
  }
  .ticket__price {
    width: 88px; background: var(--red); color: var(--white);
    font-family: "Poppins", sans-serif; font-weight: 700; font-size: 38px;
    line-height: 62px; text-align: center;
  }
  .ticket__price sup { font-size: 20px; vertical-align: 14px; }
  .venue {
    position: absolute; left: 392px; top: 906px;
    display: flex; align-items: center; gap: 3px;
    font-family: "Poppins", sans-serif; font-size: 15px; color: var(--white); letter-spacing: 0.3px;
  }
  .booking {
    position: absolute; left: 0; top: 950px; width: 100%; text-align: center;
    font-family: "Poppins", sans-serif; font-weight: 600; font-size: 13px;
    color: var(--white); letter-spacing: 0.2px;
  }
</style>
</head>
<body>
  <main class="poster">
    <div class="poster__photo" role="img" aria-label="Black and white photograph: a lone figure walking across a diagonal band of light, casting a long shadow shaped like a demon"></div>
    <p class="producer">Lanterngate Theatre Productions</p>

    <h1 class="title">
      <span class="title__the">The</span>
      <span class="title__main">Gallowmere</span>
      <span class="title__notes">Notes</span>
    </h1>

    <div class="date-box">
      <span class="date-box__day date-box__first">8<sup>TH</sup></span>
      <span class="date-box__amp">&amp;</span>
      <span class="date-box__day">15<sup>TH</sup></span>
    </div>
    <p class="month">OCTOBER</p>
    <p class="weekday">SATURDAY</p>
    <p class="showtime">7:30 PM</p>

    <p class="source">Based on <strong>R.T AMBREY'S BOOK</strong></p>
    <div class="ticket">
      <span class="ticket__label">TICKET PRICE</span>
      <span class="ticket__price"><sup>$</sup>38</span>
    </div>
    <p class="venue">
      <svg width="11" height="15" viewBox="0 0 11 15" aria-hidden="true">
        <path d="M5.5 0C2.5 0 0 2.4 0 5.4 0 9.3 5.5 15 5.5 15S11 9.3 11 5.4C11 2.4 8.5 0 5.5 0Zm0 7.6a2.2 2.2 0 1 1 0-4.4 2.2 2.2 0 0 1 0 4.4Z" fill="var(--red)"/>
      </svg>
      BRINDLECOMBE CIVIC THEATRE
    </p>
    <p class="booking">https://app.seatvane-example.org.au/LanterngateTheatreProductions/Gallowmere</p>
  </main>
</body>
</html>
```